Real Estate Sales Brokerage

Design a modern and fresh looking standard size business card, incorporate our logo's color scheme and modern appearance with head shot photo on front side and incorporate our log on the back side

Target Market(s)

Residential Home sales

Industry/Entity Type

Real Estate Agent

Font styles to use
Sans Serif

Colors

Designer to choose colors to be used in the design.

Requirements
Must have
• fresh, modern, not too busy, incorporate head shot in front of the card, incorporate logo in front and back of the card. Use logo design scheme as appropriate.
Nice to have
• horizontal and vertical options to compare would be nice.

```html
<!DOCTYPE html>
<html lang="en">
<head>
<meta charset="utf-8">
<title>Harbor Key Realty – Business Card</title>
<link href="https://fonts.googleapis.com/css2?family=Arimo:wght@400;700&display=swap" rel="stylesheet">
<style>
  :root {
    --backdrop: #1f1f1f;
    --card: #f1f1f1;
    --olive: #5b5631;
    --gold: #e4c43f;
    --ink: #474747;
    --url: #555555;
  }
  * { margin: 0; padding: 0; box-sizing: border-box; }
  html, body { width: 1200px; height: 960px; overflow: hidden; }
  body {
    background: var(--backdrop);
    font-family: "Arimo", Arial, sans-serif;
    position: relative;
  }
  .card {
    position: absolute;
    left: 314px;
    width: 600px;
    height: 343px;
    background: var(--card);
    box-shadow: 0 3px 8px rgba(0,0,0,.5);
  }
  .card--front { top: 113px; }
  .card--back { top: 472px; }

  .agent { position: absolute; left: 63px; top: 82px; }
  .agent__name {
    color: var(--olive);
    font-weight: 700;
    font-size: 22px;
    line-height: 24px;
  }
  .agent__title {
    color: var(--gold);
    font-size: 15px;
    line-height: 18px;
    margin-top: 1px;
  }
  .agent__address {
    color: var(--ink);
    font-size: 14px;
    line-height: 18px;
    margin-top: 12px;
  }
  .contact { list-style: none; margin-top: 10px; }
  .contact__item {
    display: flex;
    align-items: center;
    color: var(--ink);
    font-size: 14px;
    line-height: 19.5px;
  }
  .contact__icon { width: 13px; height: 13px; margin-right: 9px; fill: var(--ink); }

  .headshot {
    position: absolute;
    left: 370px;
    top: 67px;
    width: 161px;
    height: 203px;
    border-radius: 8px;
    background: linear-gradient(180deg, #cfd3d4 0%, #c3c7c8 45%, #2f4d86 70%, #243d6c 100%);
  }

  .brand {
    position: absolute;
    left: 0; right: 0;
    top: 130px;
    display: flex;
    justify-content: center;
    align-items: center;
    gap: 14px;
  }
  .brand__mark { width: 18px; height: 18px; background: var(--olive); }
  .brand__name {
    color: var(--olive);
    font-size: 30px;
    font-weight: 400;
    letter-spacing: .5px;
  }
  .brand__url {
    position: absolute;
    left: 0; right: 0;
    top: 286px;
    text-align: center;
    color: var(--url);
    font-size: 15px;
    letter-spacing: 5px;
  }
</style>
</head>
<body>
  <section class="card card--front">
    <div class="agent">
      <h1 class="agent__name">DANIEL MARSH</h1>
      <p class="agent__title">CEO/FOUNDER</p>
      <p class="agent__address">4120 Willow Crest Drive<br>Juneau, Alaska 99801</p>
      <ul class="contact">
        <li class="contact__item">
          <svg class="contact__icon" viewBox="0 0 16 16"><path d="M3.5 1l3 3-1.6 2a9 9 0 0 0 5 5l2-1.6 3 3-2 2C6 14 2 10 1.5 3z"/></svg>
          555 204 7716
        </li>
        <li class="contact__item">
          <svg class="contact__icon" viewBox="0 0 16 16"><path d="M4 0h8a1 1 0 0 1 1 1v14a1 1 0 0 1-1 1H4a1 1 0 0 1-1-1V1a1 1 0 0 1 1-1zm1 2v10h6V2zm3 11a1 1 0 1 0 0 2 1 1 0 0 0 0-2z"/></svg>
          555 318 6042
        </li>
        <li class="contact__item">
          <svg class="contact__icon" viewBox="0 0 16 16"><path d="M1 3h14v10H1zm1 1.2V5l6 4 6-4v-.8z"/></svg>
          name@harborkeyrealty.com
        </li>
        <li class="contact__item">
          <svg class="contact__icon" viewBox="0 0 16 16"><circle cx="8" cy="8" r="7"/><path d="M1 8h14M8 1c-3 3-3 11 0 14M8 1c3 3 3 11 0 14" stroke="#f1f1f1" stroke-width="1.2" fill="none"/></svg>
          www.harborkeyrealty.com
        </li>
      </ul>
    </div>
    <div class="headshot" role="img" aria-label="Head shot of the agent in a navy suit"></div>
  </section>

  <section class="card card--back">
    <div class="brand">
      <span class="brand__mark"></span>
      <span class="brand__name">HARBOR KEY REALTY</span>
    </div>
    <p class="brand__url">www.harborkeyrealty.com</p>
  </section>
</body>
</html>
```